Brightwell is a company offering Colon Hydrotherapy (or colonics)

Brightwell offers Colon Hydrotherapy using an innovative FDA approved system from the USA. The system is called the TORVA system. The clinic is based in Whangarei, Northland and is the first business of this kind for Northland.
I used to use a design from the Printlane website - a water symbol. However, I want a design that will convey freshness. I want something new and clean which conveys vitality and revitalisation .... perhaps water or bubbles but which brings across the idea of detoxing (which is what colon hydrotherapy does)
The clinic will only be completed in April so for now I have put my mobile number but once in the clinic this will need to be changed to a landline number ... the email address will also change. Thanks for any ideas you give me,
Updates

Hi. I need the name Brightwell first and foremost as this is the name of the Company Underneath this it has to say Colon Hydrotherapy to let people know what Brightwell is My name underneath that would be Miriam Holloway And all contact details to follow this. Thanks !

Target Market(s)

People who are wanting to "detox" and focusing on their health and wellbeing

Industry/Entity Type

Clinic

Contact Information for Business Card

Brightwell
Colon Hydrotherapy
Miriam Holloway
Unit B, 42c Harbour Lane, Whangarei

021 0487 3926
brightwellcare@mailnest.example

Font styles to use
Serif

Colors
cee9f6
33a6d7
86cae6

Requirements
Must have
• Stand out with colour or logo

```html
<!DOCTYPE html>
<html lang="en">
<head>
<meta charset="utf-8">
<title>Brightwell Colon Hydrotherapy – Business Card</title>
<link rel="stylesheet" href="https://fonts.googleapis.com/css2?family=Tinos&display=swap">
<style>
  :root {
    --page-bg: #eef1f5;
    --card-blue: #5a7ec4;
    --card-blue-light: #6488cc;
    --card-blue-deep: #5276bd;
    --ink-white: #ffffff;
    --placeholder-top: #7a9ad4;
    --placeholder-bottom: #86a9dc;
  }
  * { box-sizing: border-box; margin: 0; padding: 0; }
  html, body {
    width: 1200px;
    height: 886px;
    overflow: hidden;
    background: var(--page-bg);
  }
  .sheet {
    width: 1200px;
    height: 886px;
    display: flex;
    flex-direction: column;
    align-items: center;
    justify-content: center;
    gap: 56px;
  }
  .card {
    position: relative;
    width: 640px;
    height: 366px;
    background: linear-gradient(135deg, var(--card-blue-light) 0%, var(--card-blue) 50%, var(--card-blue-deep) 100%);
    color: var(--ink-white);
    font-family: "Tinos", "Times New Roman", serif;
    box-shadow: 0 10px 24px rgba(40, 60, 100, 0.22);
    overflow: hidden;
  }
  .illustration {
    position: absolute;
    border-radius: 6px;
    background: linear-gradient(180deg, var(--placeholder-top), var(--placeholder-bottom));
  }
  .card-front .illustration {
    left: 478px;
    top: 30px;
    width: 136px;
    height: 112px;
  }
  .brand {
    position: absolute;
    left: 38px;
    top: 64px;
    font-size: 32px;
    font-weight: 400;
    letter-spacing: 0.3px;
    white-space: nowrap;
  }
  .holder {
    position: absolute;
    left: 108px;
    top: 150px;
    font-size: 24px;
    font-weight: 400;
  }
  .contact {
    position: absolute;
    left: 148px;
    top: 214px;
    list-style: none;
    font-size: 15px;
    line-height: 26px;
  }
  .contact li { display: flex; align-items: center; gap: 10px; white-space: nowrap; }
  .contact .icon { width: 14px; height: 14px; flex: none; }

  .card-back .illustration {
    left: 360px;
    top: 56px;
    width: 190px;
    height: 112px;
  }
  .tagline {
    position: absolute;
    left: 60px;
    bottom: 72px;
    font-size: 44px;
    font-weight: 400;
    white-space: nowrap;
  }
</style>
</head>
<body>
<main class="sheet">
  <section class="card card-front" aria-label="Business card front">
    <div class="illustration" role="img" aria-label="Water droplet illustration"></div>
    <h1 class="brand">Brightwell Colon Hydrotherapy</h1>
    <p class="holder">Miriam Holloway</p>
    <ul class="contact">
      <li>Unit B, 42c Harbour Lane, Whangarei</li>
      <li>
        <svg class="icon" viewBox="0 0 16 16" aria-hidden="true">
          <path d="M2 6 Q8 1 14 6 L12 7.5 L10.5 5.5 H5.5 L4 7.5 Z" fill="#fff"/>
          <rect x="3.5" y="8" width="9" height="6" rx="1" fill="#fff"/>
        </svg>
        <span>021 0487 3926</span>
      </li>
      <li>
        <svg class="icon" viewBox="0 0 16 16" aria-hidden="true">
          <rect x="1" y="3.5" width="14" height="9" fill="#fff"/>
          <path d="M1 3.5 L8 9 L15 3.5" fill="none" stroke="#5a7ec4" stroke-width="1.2"/>
        </svg>
        <span>brightwellcare@mailnest.example</span>
      </li>
    </ul>
  </section>

  <section class="card card-back" aria-label="Business card back">
    <div class="illustration" role="img" aria-label="Water droplet illustration"></div>
    <p class="tagline">Colon Hydrotherapy</p>
  </section>
</main>
</body>
</html>
```